Poster Design Project

Simple, very easy design project.

Design for a 20" x 30" poster (I will print the poster, you do the high-res design), of the attached.

(Pls note, this JPG is sideways and is an error). You are designing PORTRAIT

```html
<!DOCTYPE html>
<html lang="en">
<head>
<meta charset="utf-8">
<title>Great Ecommerce</title>
<link rel="stylesheet" href="https://fonts.googleapis.com/css2?family=Open+Sans:wght@700;800&display=swap">
<style>
  :root {
    --green: #76b82a;
    --green-light: #a6e46e;
    --navy: #064b80;
    --white: #ffffff;
    --globe-line: #5a7fa8;
  }
  * { margin: 0; padding: 0; box-sizing: border-box; }
  html, body { width: 800px; height: 1200px; overflow: hidden; background: var(--white); }
  .poster {
    position: relative;
    width: 800px;
    height: 1200px;
    overflow: hidden;
    background: var(--white);
    font-family: "Open Sans", sans-serif;
  }
  .top-band {
    position: absolute; left: 0; top: 0;
    width: 800px; height: 8px;
    background: var(--green);
  }
  .title {
    position: absolute; left: 0; top: 22px; width: 800px;
    text-align: center;
    font-weight: 700;
    letter-spacing: -1px;
  }
  .title-great {
    display: block;
    color: var(--green);
    font-size: 98px;
    line-height: 98px;
    margin-left: -10px;
  }
  .title-ecommerce {
    display: block;
    color: var(--navy);
    font-size: 102px;
    line-height: 104px;
    margin-top: -6px;
  }
  .backdrop {
    position: absolute; left: 0; top: 0;
    width: 800px; height: 1200px;
  }
  .leaf-art {
    position: absolute; left: 0; top: 0;
    width: 800px; height: 1200px;
  }
  .values {
    position: absolute; left: 0; top: 0;
    list-style: none;
  }
  .value {
    position: absolute;
    left: 133px;
    display: flex;
    align-items: center;
    white-space: nowrap;
  }
  .value-icon { width: 26px; height: 26px; flex: none; }
  .value-text {
    margin-left: 54px;
    color: var(--white);
    font-weight: 700;
    font-size: 40px;
    line-height: 48px;
    text-shadow: 1px 2px 2px rgba(0, 0, 0, 0.35);
  }
</style>
</head>
<body>
<div class="poster">
  <svg class="backdrop" viewBox="0 0 1000 1500" preserveAspectRatio="none" aria-hidden="true">
    <path class="navy-field" d="M0,712 C300,795 700,705 1000,290 L1000,1500 L0,1500 Z" fill="var(--navy)"/>
  </svg>

  <svg class="leaf-art" viewBox="0 0 1000 1500" preserveAspectRatio="none" role="img"
       aria-label="Collage of white web and shopping icons: cart, magnifiers, envelope, globe, thumbs up, home, lock, chart, speaker and more">
    <path class="leaf" d="M0,640 C250,330 650,250 1000,272 L1000,292 C700,705 300,795 0,712 Z"
          fill="var(--green)" stroke="var(--green-light)" stroke-width="6"/>
  </svg>

  <div class="top-band"></div>

  <h1 class="title">
    <span class="title-great">Great</span>
    <span class="title-ecommerce">Ecommerce</span>
  </h1>

  <ul class="values">
    <li class="value" style="top:702px">
      <svg class="value-icon" viewBox="0 0 26 26" aria-hidden="true"><g fill="var(--white)" stroke="var(--globe-line)" stroke-width="1.3"><circle cx="13" cy="13" r="11.5"/><ellipse cx="13" cy="13" rx="5" ry="11.5" fill="none"/><path d="M1.5,13 H24.5 M4,7 H22 M4,19 H22 M13,1.5 V24.5" fill="none"/></g></svg>
      <span class="value-text">Diversity of Thought</span>
    </li>
    <li class="value" style="top:778px">
      <svg class="value-icon" viewBox="0 0 26 26" aria-hidden="true"><g fill="var(--white)" stroke="var(--globe-line)" stroke-width="1.3"><circle cx="13" cy="13" r="11.5"/><ellipse cx="13" cy="13" rx="5" ry="11.5" fill="none"/><path d="M1.5,13 H24.5 M4,7 H22 M4,19 H22 M13,1.5 V24.5" fill="none"/></g></svg>
      <span class="value-text">Desire to Learn</span>
    </li>
    <li class="value" style="top:851px">
      <svg class="value-icon" viewBox="0 0 26 26" aria-hidden="true"><g fill="var(--white)" stroke="var(--globe-line)" stroke-width="1.3"><circle cx="13" cy="13" r="11.5"/><ellipse cx="13" cy="13" rx="5" ry="11.5" fill="none"/><path d="M1.5,13 H24.5 M4,7 H22 M4,19 H22 M13,1.5 V24.5" fill="none"/></g></svg>
      <span class="value-text">Never Settle</span>
    </li>
    <li class="value" style="top:920px">
      <svg class="value-icon" viewBox="0 0 26 26" aria-hidden="true"><g fill="var(--white)" stroke="var(--globe-line)" stroke-width="1.3"><circle cx="13" cy="13" r="11.5"/><ellipse cx="13" cy="13" rx="5" ry="11.5" fill="none"/><path d="M1.5,13 H24.5 M4,7 H22 M4,19 H22 M13,1.5 V24.5" fill="none"/></g></svg>
      <span class="value-text">Be a Problem Solver</span>
    </li>
    <li class="value" style="top:994px">
      <svg class="value-icon" viewBox="0 0 26 26" aria-hidden="true"><g fill="var(--white)" stroke="var(--globe-line)" stroke-width="1.3"><circle cx="13" cy="13" r="11.5"/><ellipse cx="13" cy="13" rx="5" ry="11.5" fill="none"/><path d="M1.5,13 H24.5 M4,7 H22 M4,19 H22 M13,1.5 V24.5" fill="none"/></g></svg>
      <span class="value-text" style="margin-left:56px">Work Fast (Web Speed)</span>
    </li>
    <li class="value" style="top:1067px">
      <svg class="value-icon" viewBox="0 0 26 26" aria-hidden="true"><g fill="var(--white)" stroke="var(--globe-line)" stroke-width="1.3"><circle cx="13" cy="13" r="11.5"/><ellipse cx="13" cy="13" rx="5" ry="11.5" fill="none"/><path d="M1.5,13 H24.5 M4,7 H22 M4,19 H22 M13,1.5 V24.5" fill="none"/></g></svg>
      <span class="value-text">Execution - A Way of Life</span>
    </li>
  </ul>
</div>
</body>
</html>
```